Upmarket Bathroom and Kitchen ware supplier needs a classy business card design

We are a company based in Fiji, we sell plumbing ware (Kitchen and bathroom taps, Basins,showers, toilets etc) through up market show rooms to individuals and directly through Architects and designers of resorts and holiday houses for new builds and renovations. we are wanting to upgrade our over all look and brand. we are starting with a new logo but will be rebranding the whole business. This project is for a business card design for my management and tales team I would like it to be dark, classy and interesting

Target Market(s)

Resort directors and Management, High end holiday home owners

Contact Information for Business Card

Neil Dawson
Director
+64219473815

Colors

Designer to choose colors to be used in the design.

Requirements
Must have
• Must have an upmarket appearance I like darker charcoal shades but will be guided by the designers
• Please any catch phrases like "Crafting remarkable living rooms" this belongs tpo one of our suppliers so can not be used.
Nice to have
• Double sided, so front dedicated to logo provided and back info about the business and the person.

```html
<!DOCTYPE html>
<html lang="en">
<head>
<meta charset="utf-8">
<title>Coralstone Interiors – Business Cards</title>
<link href="https://fonts.googleapis.com/css2?family=Open+Sans:wght@400;700&display=swap" rel="stylesheet">
<style>
  :root{
    --backdrop:#2a2c30;
    --card-black:#0b0b0c;
    --card-charcoal:#1a1a1c;
    --pattern-tone:#202022;
    --paper:#ffffff;
    --ink:#1a1a1a;
    --ink-soft:#4a4a4a;
    --name-light:#f2f2f2;
  }
  *{box-sizing:border-box;margin:0;padding:0}
  html,body{width:1200px;height:900px;overflow:hidden}
  body{background:var(--backdrop);position:relative;font-family:"Open Sans",Arial,sans-serif}

  .card{position:absolute;left:250px;width:700px;height:400px;overflow:hidden;box-shadow:0 10px 30px rgba(0,0,0,.45)}
  .card--info{top:36px;background:var(--paper)}
  .card--brand{top:464px;background:var(--card-charcoal)}

  /* info side */
  .info-band{position:absolute;left:0;top:0;width:100%;height:248px;background:var(--card-black)}
  .info-rule{position:absolute;left:0;top:252px;width:100%;height:3px;background:var(--paper)}
  .info-gap{position:absolute;left:0;top:255px;width:100%;height:7px;background:var(--card-black)}

  .company{display:flex;align-items:center;gap:16px;color:var(--name-light);font-family:"Open Sans",Arial,sans-serif;font-weight:400;white-space:nowrap}
  .company__dot{border:2px solid var(--name-light);border-radius:50%;flex:none}

  .info-band .company{position:absolute;left:50%;top:50%;transform:translate(-50%,-50%);font-size:34px}
  .info-band .company__dot{width:40px;height:40px}

  .person{position:absolute;left:34px;top:286px}
  .person__name{font-weight:700;font-size:22px;color:var(--ink);text-transform:uppercase;letter-spacing:.01em}
  .person__role{font-size:14px;color:var(--ink-soft);margin-top:1px}

  .contacts{position:absolute;right:30px;top:278px;list-style:none;text-align:right}
  .contacts li{display:flex;align-items:center;justify-content:flex-end;gap:10px;font-size:19px;color:var(--ink);line-height:34px}
  .contacts strong{font-weight:700}
  .contacts svg{width:17px;height:17px;flex:none}

  /* brand side */
  .brand-pattern{position:absolute;inset:0;background:linear-gradient(135deg,var(--pattern-tone),var(--card-charcoal) 60%)}
  .card--brand .company{position:absolute;left:50%;top:50%;transform:translate(-50%,-50%);font-size:22px;gap:12px}
  .card--brand .company__dot{width:26px;height:26px;border-width:1.5px}
</style>
</head>
<body>

<section class="card card--info">
  <div class="info-band">
    <p class="company"><span class="company__dot"></span>Coralstone Interiors</p>
  </div>
  <div class="info-rule"></div>
  <div class="info-gap"></div>

  <div class="person">
    <p class="person__name">Neil Dawson</p>
    <p class="person__role">Director</p>
  </div>

  <ul class="contacts">
    <li>+642 1947 3815
      <svg viewBox="0 0 24 24" aria-hidden="true"><path fill="#1a1a1a" d="M6.6 10.8a15.1 15.1 0 0 0 6.6 6.6l2.2-2.2c.3-.3.7-.4 1-.2 1.1.4 2.3.6 3.6.6.6 0 1 .4 1 1V20c0 .6-.4 1-1 1A17 17 0 0 1 3 4c0-.6.4-1 1-1h3.5c.6 0 1 .4 1 1 0 1.3.2 2.5.6 3.6.1.3 0 .7-.2 1z"/></svg>
    </li>
    <li>info@coralstoneinteriors.com
      <svg viewBox="0 0 24 24" aria-hidden="true"><path fill="#1a1a1a" d="M2 5h20v14H2z"/><path fill="none" stroke="#fff" stroke-width="1.6" d="M2.5 5.5 12 13l9.5-7.5M2.5 18.5l7-6.5M21.5 18.5l-7-6.5"/></svg>
    </li>
    <li><span>www.<strong>coralstoneinteriors</strong>.com</span>
      <svg viewBox="0 0 24 24" aria-hidden="true"><circle cx="12" cy="12" r="10" fill="#1a1a1a"/><g fill="none" stroke="#fff" stroke-width="1.2"><path d="M2 12h20M12 2v20"/><ellipse cx="12" cy="12" rx="4.5" ry="10"/><path d="M4 7h16M4 17h16"/></g></svg>
    </li>
  </ul>
</section>

<section class="card card--brand">
  <div class="brand-pattern" role="img" aria-label="Faint tone-on-tone repeated pattern across the dark card"></div>
  <p class="company"><span class="company__dot"></span>Coralstone Interiors</p>
</section>

</body>
</html>
```